Redesign the *Settings* screen for the BrelloZ app.

BrelloZ app is in production, but we need to refresh and redesign the settings screen to be cleaner, easier, more intuitive, and more professional looking.

Project Deadline Extended
Reason: Several designers have requested more time. This will also give time to provide feedback on existing designs.

Requirements
Must have
• Black background, so that the screen is consistent with the rest of the app.

```html
<!DOCTYPE html>
<html lang="en">
<head>
<meta charset="utf-8">
<title>BrelloZ — Settings</title>
<link href="https://fonts.googleapis.com/css2?family=Montserrat:wght@400;500;600&display=swap" rel="stylesheet">
<style>
  :root {
    --page-bg: #161e26;
    --screen-top: #333645;
    --screen-bottom: #232634;
    --tile: #2c3045;
    --tile-dim-text: #5a5f74;
    --accent-a: #dd5418;
    --accent-b: #dd2f3c;
    --accent: #e2452a;
    --text: #ffffff;
    --ring: #3a3d4a;
    --tabbar: #1f2432;
  }
  * { box-sizing: border-box; margin: 0; padding: 0; }
  html, body { width: 1200px; height: 1200px; overflow: hidden; }
  body {
    background: var(--page-bg);
    font-family: "Montserrat", sans-serif;
    color: var(--text);
    display: flex; align-items: center; justify-content: center;
  }
  .screen {
    position: relative;
    width: 600px; height: 1067px;
    background: linear-gradient(160deg, var(--screen-top), var(--screen-bottom) 60%);
    overflow: hidden;
  }
  .status-bar {
    height: 36px; padding: 0 18px;
    display: flex; align-items: center; justify-content: space-between;
    font-size: 15px; font-weight: 500;
    background: rgba(0,0,0,0.12);
  }
  .status-bar .signal { letter-spacing: 1px; }
  .status-right { display: flex; align-items: center; gap: 8px; }
  .battery { width: 28px; height: 13px; background: var(--text); border-radius: 3px; }

  .dial { position: absolute; left: 100px; top: 100px; width: 400px; height: 420px; }
  .weapon-art {
    position: absolute; left: 140px; top: 115px; width: 120px; height: 95px;
    background: linear-gradient(135deg, rgba(226,69,42,0.55), rgba(221,47,60,0.25));
    border-radius: 6px;
  }
  .weapon-name {
    position: absolute; left: 0; width: 400px; top: 225px; text-align: center;
    color: var(--accent); font-size: 34px; font-weight: 500; letter-spacing: 2px;
  }

  .settings { position: absolute; left: 24px; right: 24px; top: 520px; }
  .group-label { font-size: 22px; font-weight: 500; margin: 0 0 14px 4px; }
  .group { margin-bottom: 30px; }
  .options { display: grid; gap: 12px; }
  .options.two { grid-template-columns: 1fr 1fr; }
  .options.three { grid-template-columns: 1fr 1fr 1fr; }
  .option {
    height: 80px; background: var(--tile);
    display: flex; align-items: center; justify-content: center; gap: 14px;
    font-size: 20px; font-weight: 500; letter-spacing: 2px; text-transform: uppercase;
    color: var(--text);
  }
  .option.dim { color: var(--tile-dim-text); }
  .option.active { background: linear-gradient(90deg, var(--accent-a), var(--accent-b)); }
  .option-icon {
    width: 24px; height: 24px; border: 2px solid currentColor; border-radius: 5px;
    display: inline-block;
  }
  .sub { font-size: 12px; vertical-align: sub; }

  .tab-bar {
    position: absolute; left: 0; right: 0; bottom: 0; height: 96px;
    background: var(--tabbar);
    display: grid; grid-template-columns: repeat(4, 1fr);
  }
  .tab {
    display: flex; flex-direction: column; align-items: center; justify-content: center; gap: 8px;
    font-size: 13px; letter-spacing: 2px; font-weight: 500;
  }
  .tab.active { color: var(--accent); }
  .tab svg { width: 34px; height: 34px; fill: none; stroke: currentColor; stroke-width: 2; }
</style>
</head>
<body>
<main class="screen">
  <header class="status-bar">
    <span class="signal">●●○○○ Nimbus</span>
    <span>10:07 AM</span>
    <span class="status-right"><span>✱</span><span>68%</span><span class="battery"></span></span>
  </header>

  <section class="dial">
    <svg width="400" height="420" viewBox="0 0 400 420">
      <circle cx="200" cy="200" r="180" fill="none" stroke="var(--ring)" stroke-width="4" stroke-dasharray="170 14" transform="rotate(-100 200 200)"/>
      <path d="M369.1 261.6 A180 180 0 0 1 184.3 379.3" fill="none" stroke="var(--accent)" stroke-width="4"/>
      <polygon points="318,372 334,376 322,388" fill="var(--accent)"/>
    </svg>
    <div class="weapon-art" role="img" aria-label="Outline drawing of the selected pistol"></div>
    <div class="weapon-name">R340</div>
  </section>

  <section class="settings">
    <div class="group">
      <h2 class="group-label">Hand</h2>
      <div class="options two">
        <div class="option dim"><span class="option-icon" role="img" aria-label="Right hand icon"></span>Right</div>
        <div class="option active"><span class="option-icon" role="img" aria-label="Left hand icon"></span>Left</div>
      </div>
    </div>
    <div class="group">
      <h2 class="group-label">Dry Practise</h2>
      <div class="options three">
        <div class="option active"><span class="option-icon" role="img" aria-label="Cartridge icon"></span></div>
        <div class="option"><span class="option-icon" role="img" aria-label="Book icon"></span></div>
        <div class="option">CO<span class="sub">2</span></div>
      </div>
    </div>
    <div class="group">
      <h2 class="group-label">Device Mount Position</h2>
      <div class="options three">
        <div class="option dim">Under</div>
        <div class="option dim">Side</div>
        <div class="option active">Rail</div>
      </div>
    </div>
  </section>

  <nav class="tab-bar">
    <div class="tab">
      <svg viewBox="0 0 34 34"><circle cx="17" cy="17" r="12"/><circle cx="17" cy="17" r="4" fill="currentColor"/><path d="M17 1v6M17 27v6M1 17h6M27 17h6"/></svg>
      TRAIN
    </div>
    <div class="tab">
      <svg viewBox="0 0 34 34"><path d="M3 30V20h8v10M11 30V12h8v18M19 30V5h8v25M3 30h28"/></svg>
      HISTORY
    </div>
    <div class="tab">
      <svg viewBox="0 0 34 34"><path d="M2 13l15-7 15 7-15 7z M8 16v8c5 4 13 4 18 0v-8 M30 14v9"/></svg>
      LEARN
    </div>
    <div class="tab active">
      <svg viewBox="0 0 34 34"><circle cx="17" cy="17" r="5"/><path d="M17 3v5M17 26v5M3 17h5M26 17h5M7 7l4 4M23 23l4 4M27 7l-4 4M11 23l-4 4"/><circle cx="17" cy="17" r="10"/></svg>
      SETTINGS
    </div>
  </nav>
</main>
</body>
</html>
```